Elegant and modern body scrub for organic junkies

I need a package design for my new company based out of Austin, Texas. We are focused on cruelty free and all natural and organic products. Our deign needs to be able to have the information we require on it, while still appearing very clean and captivating. Our initial product is a clear skin body scrub, intended for people with problematic skin. Our target market is women and we want to show elegance, without appearing "high end."
Updates

Reason: I want to allot more time for certain designers to submit edits. Last minute proposals have been appealing

Target Market(s)

Women. Organic and holistic minded. Natural beauty lovers.

Industry/Entity Type

Skin Care Product

Font styles to use
Script
Other font styles liked:
• AmericanTypewriter, Beautifulflaws, courier, caviarDreams-bold

Colors
000000
ffc214
ffffff
fece3e
fbee3e

Requirements
Must have
• Must be designed in Adobe Illustrator.
• The photo titled “structure for oz and grams” -That needs to be included at the bottom of 1B. I like the horizontal and vertical bar that separate the two. I want that.
• Color Inspiration - The photo titled “venra color inspiration” and “color combo inspiration” are the colors I want. BLACK, GOLD, WHITE. I want the label background black and the writing in white with some gold somewhere on it. My logo is going to be a golden elephant.
• The photos titled “I like how clean this looks” and “I also like how clean this looks” - I want 1B to look super clean. I don’t want a lot of information in this box. I want simple and clean. This is where the logo and brand name will go.
• Logo - A golden elephant. I want it to be gold and geometric. There can be dimension like this elephant example on the left of the 1B description. I want the trunk to be facing to the left and the trunk needs to be raised overhead and touching the animal's forehead.
• The photo titled “sideways writing and silver rim” - I want 1C to be written sideways like this. My text will be much more extensive so the font won’t be able to be so big.
Nice to have
• The photo titled “sideways writing and silver rim” - I want 1C to be written sideways like this. My text will be much more extensive so the font won’t be able to be so big. I also REALLY like how this label is rimmed in silver, but I would want gold. This is not mandatory, but I really like this.
• The photo titled “melted honey” - This is another option I really like. The gold that looks like honey dripping on the label is really cool. Not mandatory, but I really liked that. I also like the craft background on this.
• Color Inspiration - The photo titled “color inspiration” and “another color inspiration” is an option I would also like to see. Rather than black, I’d like to see what it would ALSO look like with a navy background. NAVY, GOLD, WHITE, maybe black somewhere.
Should not have
• Colorful patterns or excessive info in section 1B.

```html
<!DOCTYPE html>
<html lang="en">
<head>
<meta charset="UTF-8">
<title>Clear Skin Body Polish – Jar Label</title>
<link href="https://fonts.googleapis.com/css2?family=Sacramento&family=Raleway:wght@400;500&family=Courier+Prime&family=Arimo:ital,wght@0,400;1,700&display=swap" rel="stylesheet">
<style>
  :root {
    --navy: #111c3b;
    --gold: #f0c57e;
    --gold-deep: #d7a95c;
    --white: #ffffff;
    --muted: #d9dbe2;
    --page: #ffffff;
    --script: "Sacramento", cursive;
    --caps: "Raleway", sans-serif;
    --body: "Arimo", Arial, sans-serif;
    --mono: "Courier Prime", "Courier New", monospace;
  }
  * { box-sizing: border-box; margin: 0; padding: 0; }
  html, body { width: 1200px; height: 770px; overflow: hidden; background: var(--page); }
  .canvas { position: relative; width: 1200px; height: 770px; }

  .label {
    position: absolute; left: 10px; top: 280px;
    width: 1180px; height: 205px;
    background: var(--navy); color: var(--white);
    overflow: hidden;
  }
  .label__drip { position: absolute; left: 0; top: 0; width: 1180px; height: 40px; }

  .script-heading {
    position: absolute; font-family: var(--script); font-weight: 400; color: var(--gold);
    font-size: 24px; line-height: 1; white-space: nowrap;
  }

  /* Left panel */
  .info { position: absolute; left: 8px; top: 0; width: 390px; }
  .info .script-heading { left: 10px; top: 20px; }
  .claims {
    position: absolute; left: 4px; top: 46px; width: 342px; height: 26px;
    border: 1px solid var(--gold); display: flex;
  }
  .claims__item {
    font-family: var(--caps); font-size: 7.4px; letter-spacing: 0.8px;
    line-height: 1.3; text-transform: uppercase; padding: 2px 6px;
    display: flex; align-items: center;
  }
  .claims__item + .claims__item { border-left: 1px solid var(--gold); }
  .claims__item--organic { width: 60px; }
  .claims__item--animals { width: 94px; }
  .claims__item--free { flex: 1; }
  .copy { font-family: var(--body); font-size: 7.8px; line-height: 1.32; }
  .info .copy { position: absolute; left: 4px; top: 77px; width: 372px; }
  .copy p + p { margin-top: 4px; }
  .copy strong { font-style: italic; font-weight: 700; }
  .recycle {
    position: absolute; left: 8px; top: 176px; display: flex; align-items: center; gap: 8px;
    font-family: var(--caps); font-size: 9px; letter-spacing: 0.3px; color: var(--muted);
  }

  /* Centre panel */
  .brand { position: absolute; left: 405px; top: 0; width: 320px; height: 205px; }
  .brand__emblem {
    position: absolute; left: 0; top: 44px; width: 118px; height: 128px;
    border-radius: 48% 48% 20% 20%;
    background: linear-gradient(160deg, var(--gold), var(--gold-deep));
  }
  .brand__name {
    position: absolute; left: 112px; top: 134px;
    font-family: var(--script); font-weight: 400; color: var(--white);
    font-size: 22px; line-height: 1; white-space: nowrap;
  }
  .brand__rule { position: absolute; left: 108px; top: 161px; width: 185px; height: 1px; background: var(--gold); }
  .size {
    position: absolute; left: 108px; top: 166px; width: 185px; display: flex; align-items: center;
    font-family: var(--mono); font-size: 14px; color: var(--white);
  }
  .size span { flex: 1; text-align: center; }
  .size__bar { flex: 0 0 1px !important; background: var(--gold); height: 17px; }

  /* Right panel */
  .story { position: absolute; left: 748px; top: 0; width: 352px; }
  .story .script-heading { left: 4px; top: 20px; }
  .story .copy { position: absolute; left: 4px; top: 57px; width: 346px; }

  .label__blank { position: absolute; left: 1109px; top: 14px; width: 69px; height: 166px; background: var(--white); }
</style>
</head>
<body>
<main class="canvas">
  <section class="label" aria-label="Clear Skin Body Polish jar label">
    <svg class="label__drip" viewBox="0 0 1180 40" preserveAspectRatio="none" aria-hidden="true">
      <path fill="var(--gold)" d="M0 0H1180V10C1160 10 1150 16 1130 14C1110 12 1100 20 1080 16C1060 12 1050 12 1030 14C1010 16 1000 10 980 12C960 14 955 22 940 20C920 18 910 10 880 12C860 13 850 9 820 11C800 12 790 10 770 12C750 14 745 24 730 22C715 20 712 12 690 12C670 12 660 14 640 12C620 10 615 18 600 18C585 18 580 10 560 10C540 10 530 13 510 12C490 11 480 8 460 10C445 12 440 30 430 30C420 30 418 14 400 12C380 10 370 13 350 12C330 11 320 8 300 10C280 12 270 10 250 11C230 12 220 8 200 10C180 12 170 9 150 10C130 11 120 8 100 10C80 12 70 9 50 10C30 11 15 8 0 10Z"/>
    </svg>

    <div class="info">
      <h2 class="script-heading">Handmade in small batches with Love</h2>
      <div class="claims">
        <div class="claims__item claims__item--organic">All Organic</div>
        <div class="claims__item claims__item--animals">Never tested on animals</div>
        <div class="claims__item claims__item--free">Free of: fragrance, parabens, synthetic ingredients, chemicals</div>
      </div>
      <div class="copy">
        <p><strong>Ingredients:</strong> Dead Sea Salt, Pink Himalayan Salt, Coconut oil, Argan Oil, Jojoba Oil, Almond Oil, Lavender EO, Tea Tree EO, Geranium EO, Chamomile EO, Frankincense EO, Bergamot EO, Rosemary EO.</p>
        <p>Directions:: Shake well before use. Gently massage scrub in circular motions over wet skin (not face). Pay special attention to rough or dry patches. After use, a residual layer of oil will remain on skin. Rinse thoroughly and pat dry with towel. Skin will feel elegantly soft and nourished. Avoid use on freshly shaven or broken skin.</p>
        <p>Caution: Oils in product may leave shower or tub surfaces slippery. Not intended for facial use. Essential oils or use on freshly shaven skin may cause skin irritation. External use only.</p>
      </div>
      <div class="recycle">
        <svg width="14" height="14" viewBox="0 0 24 24" aria-hidden="true" fill="none" stroke="#9aa0b0" stroke-width="2">
          <path d="M12 3l4 7h-8z M4 19l4-7 4 7z M20 19h-8l4-7z" stroke-linejoin="round"/>
        </svg>
        <span>Please recycle. I want to come back as a solar panel.</span>
      </div>
    </div>

    <div class="brand">
      <div class="brand__emblem" role="img" aria-label="Golden elephant illustration with raised trunk"></div>
      <h1 class="brand__name">Clear Skin Body polish</h1>
      <div class="brand__rule"></div>
      <div class="size"><span>12oz</span><span class="size__bar"></span><span>340g</span></div>
    </div>

    <div class="story">
      <h2 class="script-heading">Made with naturally derived ingredients only</h2>
      <div class="copy">
        <p>The combination of ingredients in this loving scrub were chosen with problematic body skin in mind. The high concentration of magnesium in Dead Sea Salt is instrumental in improving skin hydration and reducing inflammation.</p>
        <p>Pink salt is readily absorbed into the skin, cleansing and purifying the pores from the inside out. It can improve the texture, tone, and appearance of the skin.</p>
        <p>This loving essential oil concoction helps fight acne by removing toxins and cleaning sebaceous glands. Some EOs contain strong antibacterial, antifungal, and anti inflammatory properties. Certain EOs inhibit the bacteria that cause skin infections as well as target acne scarring and pigmentation from previous breakouts.</p>
        <p>Each of these ingredients plays an elemental role in anti aging, as well as fighting problematic skin. Use this skin polish regularly to receive prime results.</p>
      </div>
    </div>

    <div class="label__blank"></div>
  </section>
</main>
</body>
</html>
```